Boat and Caravan indoor/ outdoor storage

A new company that provides 4star indoor and outdoor storage for Boats and Caravans
Industry/Entity Type
It Company

```html
<!DOCTYPE html>
<html lang="en">
<head>
<meta charset="utf-8">
<title>Boat &amp; Caravan Storage Flyer</title>
<link href="https://fonts.googleapis.com/css2?family=Oswald:wght@400;500&family=Open+Sans:wght@400&display=swap" rel="stylesheet">
<style>
  :root {
    --teal: #1aa3b0;
    --teal-dark: #0e7884;
    --ink: #2b2b2b;
    --body: #333333;
    --paper-top: #ffffff;
    --paper-bottom: #e6e8ea;
    --photo-boat-a: #6f7f6a;
    --photo-boat-b: #b9c2c8;
    --photo-van-a: #cfd6d8;
    --photo-van-b: #8a9a80;
  }
  * { margin: 0; padding: 0; box-sizing: border-box; }
  html, body { width: 900px; height: 1200px; overflow: hidden; background: #ffffff; }
  .flyer {
    position: relative;
    width: 900px;
    height: 1200px;
    overflow: hidden;
    background: linear-gradient(180deg, var(--paper-top) 0%, var(--paper-bottom) 100%);
    font-family: 'Open Sans', Arial, sans-serif;
  }
  .shapes { position: absolute; inset: 0; }
  .about {
    position: absolute;
    left: 45px;
    top: 450px;
    width: 392px;
  }
  .about-title {
    font-family: 'Oswald', 'Arial Narrow', sans-serif;
    font-weight: 500;
    font-size: 32px;
    color: var(--teal);
    letter-spacing: 0.5px;
    margin-bottom: 8px;
  }
  .about-text {
    font-size: 15.2px;
    line-height: 1.38;
    color: var(--body);
    text-align: justify;
  }
  .headline {
    position: absolute;
    left: 478px;
    top: 505px;
    font-family: 'Oswald', 'Arial Narrow', sans-serif;
    font-weight: 500;
    color: var(--ink);
    line-height: 1.08;
    text-transform: uppercase;
  }
  .headline-main { font-size: 60px; display: block; }
  .headline-sub { font-size: 33px; display: block; margin: 2px 0 4px; }
  .headline-accent { font-size: 60px; display: block; color: var(--teal); }
  .variations {
    position: absolute;
    left: 45px;
    top: 842px;
    font-family: 'Oswald', 'Arial Narrow', sans-serif;
    font-weight: 500;
    font-size: 27px;
    line-height: 1.25;
    color: var(--ink);
    text-transform: uppercase;
    white-space: nowrap;
  }
  .variations span { display: block; }
  .website {
    position: absolute;
    left: 0;
    width: 900px;
    top: 1118px;
    text-align: center;
    font-family: 'Oswald', 'Arial Narrow', sans-serif;
    font-size: 26px;
    letter-spacing: 5px;
    color: #ffffff;
  }
</style>
</head>
<body>
<main class="flyer">
  <svg class="shapes" width="900" height="1200" viewBox="0 0 900 1200">
    <defs>
      <linearGradient id="boatPhotoTone" x1="0" y1="0" x2="0" y2="1">
        <stop offset="0" stop-color="var(--photo-boat-a)"/>
        <stop offset="0.55" stop-color="var(--photo-boat-b)"/>
        <stop offset="1" stop-color="#9a9484"/>
      </linearGradient>
      <linearGradient id="caravanPhotoTone" x1="0" y1="0" x2="0" y2="1">
        <stop offset="0" stop-color="var(--photo-van-b)"/>
        <stop offset="0.5" stop-color="var(--photo-van-a)"/>
        <stop offset="1" stop-color="#9aa28e"/>
      </linearGradient>
    </defs>

    <polygon class="hero-photo" role="img" aria-label="Photo of white motor boats stored on trailers in an outdoor yard"
             points="0,0 900,0 900,360 560,418 0,392" fill="url(#boatPhotoTone)"/>
    <polygon class="band-left-dark" points="0,392 300,420 0,440" fill="var(--teal-dark)"/>
    <polygon class="band-left" points="0,392 560,418 430,436 0,412" fill="var(--teal)"/>
    <polygon class="band-right" points="560,418 900,360 900,398 640,440" fill="var(--teal)"/>
    <polygon class="band-right-dark" points="640,440 900,398 900,420 720,446" fill="var(--teal-dark)"/>

    <polygon class="caravan-accent" points="640,770 880,730 880,790" fill="var(--teal)"/>
    <polygon class="caravan-accent-low" points="470,1010 600,940 640,1010" fill="var(--teal-dark)"/>
    <polygon class="caravan-frame" points="492,786 872,752 880,1000 470,1006" fill="none" stroke="var(--teal)" stroke-width="5"/>
    <polygon class="caravan-photo" role="img" aria-label="Photo of a white caravan parked in a storage yard"
             points="502,796 864,764 870,990 482,996" fill="url(#caravanPhotoTone)"/>

    <polygon class="footer-band-light" points="0,1030 380,1080 900,1010 900,1200 0,1200" fill="var(--teal)"/>
    <polygon class="footer-band" points="0,1060 380,1100 900,1050 900,1200 0,1200" fill="var(--teal-dark)"/>
    <rect class="footer-strip" x="0" y="1100" width="900" height="100" fill="var(--teal)"/>
  </svg>

  <section class="about">
    <h2 class="about-title">ABOUT US</h2>
    <p class="about-text">Lorem Ipsum is simply dummy text of the printing and typesetting industry. Lorem Ipsum has been the industry's standard dummy text ever since the 1500s, when an unknown printer took a galley of type and scrambled it to make a type specimen book. It has survived not only five centuries, but also the leap into electronic typesetting, remaining essentially unchanged. It was popularised in the 1960s with the release of Typemark sheets containing Lorem Ipsum passages, and more recently with desktop publishing software like Pagecraft Studio including versions of Lorem Ipsum.</p>
  </section>

  <h1 class="headline">
    <span class="headline-main">Lorem Ipsum</span>
    <span class="headline-sub">Is simplydummy text of</span>
    <span class="headline-accent">The Printing</span>
  </h1>

  <p class="variations"><span>There are many variations of</span><span>passages of Lorem Ipsum available</span></p>

  <p class="website">WWW.YOURWEBSITE.COM</p>
</main>
</body>
</html>
```